Business Cards for a small business advisory (business services)

Professional look. Same as would apply for a lawyer, accountant, or other financial services professional. Please use the logo colors

Target Market(s)

small business owners

Industry/Entity Type

Financial Servics

Contact Information for Business Card

Name: Gavin L. Whitmore, CAIA / Title: Business Advisor / Office #: (718) 294-7716 / Mobile #: (917) 382-5047 / Email: g.whitmore@clearfieldventurepartners.example / Web: www.clearfieldventurepartners.example

Font styles to use
Sans Serif

```html
<!DOCTYPE html>
<html lang="en">
<head>
<meta charset="utf-8">
<title>Clearfield Venture Partners – Business Cards</title>
<link rel="stylesheet" href="https://fonts.googleapis.com/css2?family=Montserrat:wght@600;700&family=Lato:wght@400;700&display=swap">
<style>
  :root {
    --navy: #1b3a6b;
    --green: #8cc63f;
    --white: #ffffff;
    --ink: #4a4a4a;
    --backdrop: #2b2c2e;
  }
  * { box-sizing: border-box; margin: 0; padding: 0; }
  html, body { width: 1200px; height: 952px; overflow: hidden; }
  body {
    background: var(--backdrop);
    position: relative;
    font-family: "Lato", sans-serif;
  }
  .card {
    position: absolute;
    width: 560px;
    height: 320px;
    border-radius: 4px;
    overflow: hidden;
  }

  /* Front side */
  .card--front {
    left: 580px;
    top: 110px;
    background: var(--white);
  }
  .brand {
    display: flex;
    align-items: center;
    gap: 10px;
    font-family: "Montserrat", sans-serif;
    font-weight: 700;
  }
  .brand__dot {
    width: 14px; height: 14px;
    border-radius: 50%;
    background: var(--green);
    flex: none;
  }
  .card--front .brand {
    position: absolute;
    left: 190px;
    top: 52px;
    font-size: 24px;
    color: var(--navy);
  }
  .holder {
    position: absolute;
    left: 44px;
    top: 128px;
  }
  .holder__name {
    font-family: "Montserrat", sans-serif;
    font-weight: 600;
    font-size: 17px;
    color: var(--navy);
    text-transform: uppercase;
    letter-spacing: 0.5px;
  }
  .holder__title {
    margin-top: 4px;
    font-size: 14px;
    color: #777;
  }
  .contacts {
    position: absolute;
    left: 250px;
    top: 160px;
    list-style: none;
    font-size: 13px;
    color: var(--ink);
  }
  .contacts li {
    display: flex;
    align-items: center;
    gap: 8px;
    margin-bottom: 6px;
  }
  .contacts svg { width: 15px; height: 15px; flex: none; }
  .web-band {
    position: absolute;
    left: 0; right: 0;
    bottom: 22px;
    height: 34px;
    background: var(--navy);
    display: flex;
    align-items: center;
    padding-left: 44px;
    font-size: 14px;
    letter-spacing: 1px;
    color: var(--white);
  }
  .web-band__domain { color: var(--green); }

  /* Back side */
  .card--back {
    left: 80px;
    top: 520px;
    background: var(--navy);
    display: flex;
    align-items: center;
    justify-content: center;
  }
  .card--back .brand {
    font-size: 30px;
    color: var(--white);
  }
</style>
</head>
<body>

<section class="card card--front" aria-label="Business card front">
  <div class="brand">
    <span class="brand__dot"></span>
    <span class="brand__name">Clearfield Venture Partners</span>
  </div>

  <div class="holder">
    <p class="holder__name">Gavin L. Whitmore, CAIA</p>
    <p class="holder__title">Business Advisor</p>
  </div>

  <ul class="contacts">
    <li>
      <svg viewBox="0 0 16 16" aria-hidden="true"><rect width="16" height="16" rx="3" fill="var(--green)"/><path d="M5 3.5l2 2-1 1.2c.6 1.3 1.5 2.2 2.8 2.8l1.2-1 2 2-1.2 1.5C7.5 11.8 4.2 8.5 3.5 5z" fill="#fff"/></svg>
      (718) 294-7716
    </li>
    <li>
      <svg viewBox="0 0 16 16" aria-hidden="true"><rect width="16" height="16" rx="3" fill="var(--green)"/><rect x="5" y="2.5" width="6" height="11" rx="1" fill="#fff"/><rect x="6" y="4" width="4" height="7" fill="var(--green)"/></svg>
      (917) 382-5047
    </li>
    <li>
      <svg viewBox="0 0 16 16" aria-hidden="true"><rect width="16" height="16" rx="3" fill="var(--green)"/><rect x="3" y="4.5" width="10" height="7" fill="#fff"/><path d="M3 4.5l5 4 5-4" fill="none" stroke="var(--green)" stroke-width="1.2"/></svg>
      g.whitmore@clearfieldventurepartners.example
    </li>
  </ul>

  <div class="web-band">www.<span class="web-band__domain">clearfieldventurepartners.example</span></div>
</section>

<section class="card card--back" aria-label="Business card back">
  <div class="brand">
    <span class="brand__dot"></span>
    <span class="brand__name">Clearfield Venture Partners</span>
  </div>
</section>

</body>
</html>
```